Birch Hollow Lodge & Harbour. A site that will sell our lifestyle and embody our vision.

We are after a fun interactive website for our property development.
Check out our ideas for layout and content.
Use stock videos and phots if we havent provide enough.
Ive attached our Logo.
We are easy to reach and work with. Love the crative process.1.Our Vision.. (This clicks through to vision page)
Nestled in the North East corner of Tesko Lake , Sk amidst thousands of acres of natural beauty, a unique community is taking shape. A community that connectS people, nature and play. A place to find those simpler times.

2.Explore..(This clicks through to explore page)
Discover a new life of adventure, on the lake fishing, in the bush on our trail system or maybe the local golf course.

3. Live Here..(This through to Live page)
Birch Hollow has everything you need to start living a full life based in a thriving community.
Slow down and get to know nature and your neighbors

Target Market(s)

35-65 Lake Life

Coding

Coded - Design and coding required

Number of Pages Required

5+ page

Font styles to use
Other font styles liked:
• Anntonio

Colors
00AB8E
00BBA5
67D7C9
C6EFE9
E9F9F6
F0912C
F2A743
F7CA91
FBE8D2
FDF5EE

Requirements
Nice to have
• Interactive

```html
<!DOCTYPE html>
<html lang="en">
<head>
<meta charset="utf-8">
<title>Birch Hollow Lodge &amp; Harbour</title>
<link rel="stylesheet" href="https://fonts.googleapis.com/css2?family=Antonio:wght@600;700&family=Montserrat:wght@400;500;600&display=swap">
<style>
:root{
  --orange:#F0912C;
  --orange-light:#F2A743;
  --orange-pale:#F7CA91;
  --cream:#FDF5EE;
  --ink:#1d1b19;
  --dark:#2f2a24;
  --darker:#141210;
  --text:#3b3733;
  --white:#ffffff;
}
*{margin:0;padding:0;box-sizing:border-box}
html,body{width:1200px;height:4488px;overflow:hidden}
body{background:var(--cream);font-family:"Montserrat",sans-serif;color:var(--text);position:relative}
.section{position:absolute;left:0;width:1200px;overflow:hidden}
.abs{position:absolute}
.heading{font-family:"Antonio",sans-serif;font-weight:700;color:var(--ink);letter-spacing:1px;text-transform:uppercase;line-height:1}
.btn{position:absolute;display:flex;align-items:center;justify-content:center;gap:10px;font-size:10px;font-weight:500;text-transform:uppercase;letter-spacing:.3px;white-space:nowrap}
.btn svg{width:12px;height:12px}
.btn-orange{background:var(--orange);color:var(--white)}
.btn-outline{border:1.5px solid var(--ink);color:var(--ink)}
.btn-white{background:var(--white);color:var(--ink)}
.photo{position:absolute}
.tag{position:absolute;background:var(--white);display:flex;align-items:center;gap:10px;padding-left:18px;font-size:10px;color:var(--ink);text-transform:uppercase;white-space:nowrap}
.tag svg{width:13px;height:13px;flex:none}
.vline{position:absolute;left:599px;width:1.5px;background:var(--ink)}
.hamburger{left:113px;top:62px;width:36px;height:26px;display:flex;flex-direction:column;justify-content:space-between}
.hamburger span{display:block;height:4px;background:var(--ink)}
.brand{position:absolute;left:450px;width:300px;text-align:center;font-family:"Antonio",sans-serif;font-weight:700;text-transform:uppercase;letter-spacing:1px}
.hero-title{left:0;width:1200px;top:160px;text-align:center;font-size:56px}
.dark{background:linear-gradient(180deg,var(--dark) 0%,var(--darker) 100%)}
.dark .heading{color:var(--white)}
.section-title{width:1200px;left:0;text-align:center;font-size:52px}
.subtitle{width:1200px;left:0;text-align:center;color:#e9e3dc;font-size:13px;line-height:20px}
.card{position:absolute}
.card-label{position:absolute;left:0;right:0;bottom:18px;text-align:center;font-family:"Antonio",sans-serif;font-weight:700;font-size:22px;color:var(--white);text-transform:uppercase}
.card-bar{position:absolute;left:0;right:0;bottom:0;height:34px;background:rgba(0,0,0,.45);display:flex;align-items:center;justify-content:center;gap:10px;font-size:10px;color:var(--white);text-transform:uppercase;white-space:nowrap}
.card-bar svg{width:12px;height:12px}
.round-arrow{position:absolute;width:56px;height:56px;border-radius:50%;display:flex;align-items:center;justify-content:center}
.round-arrow svg{width:22px;height:22px}
.arrow-ghost{background:rgba(255,255,255,.25)}
.arrow-solid{background:var(--white)}
.copy{font-size:12.5px;line-height:19px;color:var(--text)}
.copy p+p{margin-top:18px}
.testimonial{position:absolute;top:174px;width:381px;height:216px;background:var(--orange-light)}
.avatar{position:absolute;left:24px;top:28px;width:64px;height:64px;border-radius:50%;background:linear-gradient(160deg,#9a7a66,#5a4438);border:3px solid var(--white)}
.t-name{position:absolute;left:112px;top:36px;font-family:"Antonio",sans-serif;font-weight:600;font-size:22px;color:var(--white);text-transform:uppercase}
.stars{position:absolute;left:112px;top:70px;display:flex;gap:5px}
.stars svg{width:15px;height:15px}
.quote{position:absolute;left:262px;top:18px;font-family:"Antonio",sans-serif;font-weight:700;font-size:130px;line-height:1;color:var(--orange-pale)}
.t-text{position:absolute;left:36px;top:118px;width:300px;font-size:12px;line-height:19px;color:var(--white)}
.email{position:absolute;left:369px;top:127px;width:462px;height:33px;border:1.5px solid var(--text);background:var(--white);font-size:12px;padding-left:16px;display:flex;align-items:center;color:var(--text)}
.footer{background:var(--darker)}
.nav{left:0;width:1200px;top:169px;display:flex;justify-content:center;gap:40px;font-size:10.5px;font-weight:600;color:var(--white);text-transform:uppercase}
.social{position:absolute;top:217px;width:42px;height:42px;border-radius:50%;background:var(--orange)}
.copyright{left:0;width:1200px;top:322px;text-align:center;font-size:10.5px;color:var(--white)}
</style>
</head>
<body>

<section class="section" style="top:0;height:724px">
  <div class="abs hamburger" aria-label="Menu"><span></span><span></span><span></span></div>
  <div class="brand" style="top:56px;font-size:30px;color:var(--ink)">Birch Hollow</div>
  <div class="btn btn-orange" style="left:944px;top:63px;width:143px;height:33px">Contact us</div>

  <h1 class="heading abs hero-title">Birch Hollow Lodge &amp; Harbour</h1>

  <div class="btn btn-orange" style="left:275px;top:247px;width:188px;height:33px">Connect to people
    <svg viewBox="0 0 12 12" fill="none" stroke="currentColor" stroke-width="1.3"><path d="M1 6h10M7 2l4 4-4 4"/></svg></div>
  <div class="btn btn-outline" style="left:496px;top:247px;width:206px;height:33px">Connect to nature
    <svg viewBox="0 0 12 12" fill="none" stroke="currentColor" stroke-width="1.3"><path d="M1 6h10M7 2l4 4-4 4"/></svg></div>
  <div class="btn btn-outline" style="left:718px;top:247px;width:205px;height:33px">Connect to play
    <svg viewBox="0 0 12 12" fill="none" stroke="currentColor" stroke-width="1.3"><path d="M1 6h10M7 2l4 4-4 4"/></svg></div>

  <div class="photo" style="left:0;top:354px;width:270px;height:320px;background:linear-gradient(170deg,#6c6f6a,#3a2f28 70%,#4a3d32)" role="img" aria-label="Wooden chalet in a misty pine forest"></div>
  <div class="photo" style="left:291px;top:354px;width:618px;height:320px;background:linear-gradient(180deg,#9fb1c0 0%,#6e8798 32%,#2f4a3c 55%,#1c2f24 100%)" role="img" aria-label="Misty mountain valley covered in evergreen forest"></div>
  <div class="photo" style="left:932px;top:354px;width:268px;height:320px;background:linear-gradient(170deg,#8a8680,#6a4a34 50%,#e8e6e2 90%)" role="img" aria-label="Log house in the snow among pine trees"></div>

  <div class="tag" style="left:331px;top:338px;width:300px;height:31px">
    <svg viewBox="0 0 14 14" fill="none" stroke="currentColor" stroke-width="1.2"><path d="M7 13s4.5-4.2 4.5-7.5a4.5 4.5 0 0 0-9 0C2.5 8.8 7 13 7 13z"/><circle cx="7" cy="5.5" r="1.6"/></svg>
    Birch Hollow Lodge, Harbour</div>

  <svg class="abs" style="left:562px;top:472px" width="76" height="76" viewBox="0 0 76 76" aria-label="Play video">
    <circle cx="38" cy="38" r="36" fill="none" stroke="rgba(255,255,255,.4)" stroke-width="1.5"/>
    <circle cx="38" cy="38" r="28" fill="rgba(255,255,255,.85)"/>
    <path d="M33 29l13 9-13 9z" fill="#1d1b19"/>
  </svg>
  <div class="abs" style="left:594px;top:566px;width:12px;font-size:7px;line-height:10px;color:var(--white);text-align:center;letter-spacing:1px">S C R O L L</div>
  <div class="vline" style="top:660px;height:64px"></div>
</section>

<section class="section" style="top:724px;height:600px">
  <div class="photo" style="left:183px;top:51px;width:394px;height:450px;background:linear-gradient(180deg,#8da0b4 0%,#b7c3cc 22%,#2f4330 48%,#5a4a36 72%,#4e5a2e 100%)" role="img" aria-label="Lakeside cabin with wraparound porch beneath tall pines"></div>
  <div class="tag" style="left:334px;top:485px;width:230px;height:31px">
    <svg viewBox="0 0 14 14" fill="none" stroke="currentColor" stroke-width="1.2"><path d="M7 13s4.5-4.2 4.5-7.5a4.5 4.5 0 0 0-9 0C2.5 8.8 7 13 7 13z"/><circle cx="7" cy="5.5" r="1.6"/></svg>
    Birch Hollow Lodge, Harbour</div>

  <h2 class="heading abs" style="left:674px;top:100px;font-size:52px">About us</h2>
  <div class="abs" style="left:637px;top:170px;width:110px;height:1.5px;background:var(--ink)"></div>
  <div class="abs copy" style="left:674px;top:190px;width:400px">
    <p>Birch Hollow Lodge resort is one of the premium hotels in Harbour, it is known for efficiently serving their guests consistently with great hospitality, service and food.</p>
    <p>A property of 35 spacious rooms located amidst the majestic mountains along with the picturesque view of lush green valleys from all rooms.</p>
    <p>Birch Hollow resort is the ideal destination for leisure vacations, business conferences and adventurous vacation.</p>
  </div>
  <div class="btn btn-orange" style="left:674px;top:405px;width:152px;height:33px">Learn more
    <svg viewBox="0 0 12 12" fill="none" stroke="currentColor" stroke-width="1.3"><path d="M1 6h10M7 2l4 4-4 4"/></svg></div>
</section>

<section class="section dark" style="top:1324px;height:732px">
  <div class="abs" style="left:413px;top:82px;width:78px;height:1.5px;background:rgba(255,255,255,.6)"></div>
  <h2 class="heading abs section-title" style="top:58px">Explore</h2>
  <p class="abs subtitle" style="top:121px">Discover &nbsp;a new life of adventure, on the lake fishing, in the bush on our trail system<br>or maybe the local golf course.</p>

  <div class="card" style="left:0;top:195px;width:91px;height:362px;background:linear-gradient(180deg,#7f9a6a,#4d6a36)" role="img" aria-label="Golfer on a green fairway"></div>
  <div class="card" style="left:111px;top:195px;width:311px;height:362px;background:linear-gradient(180deg,#9fb0b8 0%,#3d5a32 35%,#56705c 60%,#7a6a52 100%)" role="img" aria-label="Man fishing from a wooden dock on a lake">
    <div class="card-label">Lake fishing</div></div>
  <div class="card" style="left:444px;top:219px;width:310px;height:363px;background:linear-gradient(180deg,#3d3a1e 0%,#5a5a2a 40%,#6a4a2e 75%,#3a2c1e 100%)" role="img" aria-label="Hiker with a backpack on a forest trail">
    <div class="card-label">Adventure</div></div>
  <div class="card" style="left:775px;top:195px;width:310px;height:362px;background:linear-gradient(180deg,#a9b3b8 0%,#6b8452 45%,#4f6b30 100%)" role="img" aria-label="Golfer mid-swing on a golf course">
    <div class="card-label">Golf course</div></div>
  <div class="card" style="left:1108px;top:195px;width:92px;height:362px;background:linear-gradient(180deg,#7a8a86,#4a5a54)" role="img" aria-label="Angler wading in a river"></div>

  <div class="round-arrow arrow-ghost" style="left:82px;top:348px">
    <svg viewBox="0 0 22 22" fill="none" stroke="#fff" stroke-width="1.5"><path d="M19 11H3M9 5l-6 6 6 6"/></svg></div>
  <div class="round-arrow arrow-solid" style="left:1061px;top:348px">
    <svg viewBox="0 0 22 22" fill="none" stroke="#1d1b19" stroke-width="1.5"><path d="M3 11h16M13 5l6 6-6 6"/></svg></div>

  <div class="btn btn-white" style="left:523px;top:624px;width:153px;height:31px">View more
    <svg viewBox="0 0 12 12" fill="none" stroke="currentColor" stroke-width="1.3"><path d="M1 6h10M7 2l4 4-4 4"/></svg></div>
  <div class="vline" style="top:693px;height:39px;background:rgba(255,255,255,.6)"></div>
</section>

<section class="section" style="top:2056px;height:557px">
  <div class="vline" style="top:0;height:34px"></div>

  <h2 class="heading abs" style="left:183px;top:160px;font-size:52px">Our vision</h2>
  <div class="abs" style="left:348px;top:228px;width:79px;height:1.5px;background:var(--ink)"></div>
  <p class="abs copy" style="left:183px;top:251px;width:318px">Nestled in the North East corner of Tesko Lake , Sk amidst thousands of acres of natural beauty, a unique community is taking shape. A community that connectS people, nature and play. A place to find those simpler times.</p>
  <div class="btn btn-orange" style="left:183px;top:377px;width:153px;height:31px">Learn more
    <svg viewBox="0 0 12 12" fill="none" stroke="currentColor" stroke-width="1.3"><path d="M1 6h10M7 2l4 4-4 4"/></svg></div>

  <div class="photo" style="left:604px;top:118px;width:412px;height:359px;background:linear-gradient(180deg,#a8bcc4 0%,#2c4a2e 25%,#1f3a24 62%,#5a7a38 78%,#6e8a42 100%)" role="img" aria-label="Stand of spruce trees beside a grassy meadow"></div>
</section>

<section class="section dark" style="top:2613px;height:685px">
  <div class="abs" style="left:407px;top:82px;width:78px;height:1.5px;background:rgba(255,255,255,.6)"></div>
  <h2 class="heading abs section-title" style="top:56px">Live here</h2>
  <p class="abs subtitle" style="top:122px">Birch Hollow has everything you need to start living a full life based in a thriving community.</p>

  <div class="card" style="left:0;top:174px;width:91px;height:338px;background:linear-gradient(180deg,#5a7a5a,#2e4a3e)" role="img" aria-label="Lakeside homes among trees"></div>
  <div class="card" style="left:111px;top:174px;width:311px;height:338px;background:linear-gradient(180deg,#a8b8b8 0%,#2e4a32 35%,#6a4a30 65%,#2a3a3a 100%)" role="img" aria-label="Timber lodge on the water surrounded by forest">
    <div class="card-bar"><svg viewBox="0 0 14 14" fill="none" stroke="currentColor" stroke-width="1.2"><path d="M7 13s4.5-4.2 4.5-7.5a4.5 4.5 0 0 0-9 0C2.5 8.8 7 13 7 13z"/><circle cx="7" cy="5.5" r="1.6"/></svg>No. 418, Lakeshore Road</div></div>
  <div class="card" style="left:444px;top:199px;width:310px;height:338px;background:linear-gradient(180deg,#7d8a96 0%,#5e6a78 45%,#6a3a34 75%,#4a2a28 100%)" role="img" aria-label="Person standing at the end of a red dock on a foggy lake">
    <div class="card-bar"><svg viewBox="0 0 14 14" fill="none" stroke="currentColor" stroke-width="1.2"><path d="M7 13s4.5-4.2 4.5-7.5a4.5 4.5 0 0 0-9 0C2.5 8.8 7 13 7 13z"/><circle cx="7" cy="5.5" r="1.6"/></svg>Heron Lake, Harbour</div></div>
  <div class="card" style="left:775px;top:174px;width:310px;height:338px;background:linear-gradient(180deg,#9aa0a4 0%,#6a7a5a 40%,#4a5a4a 70%,#8a7a50 100%)" role="img" aria-label="Modern lake house reflected in a calm pond">
    <div class="card-bar"><svg viewBox="0 0 14 14" fill="none" stroke="currentColor" stroke-width="1.2"><path d="M7 13s4.5-4.2 4.5-7.5a4.5 4.5 0 0 0-9 0C2.5 8.8 7 13 7 13z"/><circle cx="7" cy="5.5" r="1.6"/></svg>Birch Hollow Lodge, Harbour</div></div>
  <div class="card" style="left:1108px;top:174px;width:92px;height:338px;background:linear-gradient(180deg,#4a6a4a,#2a5a5a)" role="img" aria-label="Waterfront cottages on a turquoise lake"></div>

  <div class="round-arrow arrow-ghost" style="left:82px;top:315px">
    <svg viewBox="0 0 22 22" fill="none" stroke="#fff" stroke-width="1.5"><path d="M19 11H3M9 5l-6 6 6 6"/></svg></div>
  <div class="round-arrow arrow-solid" style="left:1061px;top:315px">
    <svg viewBox="0 0 22 22" fill="none" stroke="#1d1b19" stroke-width="1.5"><path d="M3 11h16M13 5l6 6-6 6"/></svg></div>

  <div class="btn btn-white" style="left:523px;top:578px;width:153px;height:32px">View more
    <svg viewBox="0 0 12 12" fill="none" stroke="currentColor" stroke-width="1.3"><path d="M1 6h10M7 2l4 4-4 4"/></svg></div>
  <div class="vline" style="top:650px;height:35px;background:rgba(255,255,255,.6)"></div>
</section>

<section class="section" style="top:3298px;height:540px;background:var(--orange)">
  <div class="vline" style="top:0;height:38px"></div>
  <h2 class="heading abs" style="left:183px;top:78px;font-size:50px;color:var(--white)">Testimonial</h2>
  <div class="abs" style="left:451px;top:104px;width:79px;height:1.5px;background:rgba(255,255,255,.8)"></div>
  <div class="round-arrow" style="left:988px;top:76px;background:rgba(255,255,255,.25)">
    <svg viewBox="0 0 22 22" fill="none" stroke="#fff" stroke-width="1.5"><path d="M19 11H3M9 5l-6 6 6 6"/></svg></div>
  <div class="round-arrow arrow-solid" style="left:1061px;top:76px">
    <svg viewBox="0 0 22 22" fill="none" stroke="#1d1b19" stroke-width="1.5"><path d="M3 11h16M13 5l6 6-6 6"/></svg></div>

  <article class="testimonial" style="left:183px">
    <div class="avatar" role="img" aria-label="Guest portrait"></div>
    <div class="t-name">Maya R.</div>
    <div class="stars">
      <svg viewBox="0 0 16 16"><path d="M8 1l2.1 4.6 5 .5-3.8 3.3 1.1 4.9L8 11.8 3.6 14.3l1.1-4.9L.9 6.1l5-.5z" fill="#fff"/></svg>
      <svg viewBox="0 0 16 16"><path d="M8 1l2.1 4.6 5 .5-3.8 3.3 1.1 4.9L8 11.8 3.6 14.3l1.1-4.9L.9 6.1l5-.5z" fill="#fff"/></svg>
      <svg viewBox="0 0 16 16"><path d="M8 1l2.1 4.6 5 .5-3.8 3.3 1.1 4.9L8 11.8 3.6 14.3l1.1-4.9L.9 6.1l5-.5z" fill="#fff"/></svg>
      <svg viewBox="0 0 16 16"><path d="M8 1l2.1 4.6 5 .5-3.8 3.3 1.1 4.9L8 11.8 3.6 14.3l1.1-4.9L.9 6.1l5-.5z" fill="#F7CA91"/></svg>
      <svg viewBox="0 0 16 16"><path d="M8 1l2.1 4.6 5 .5-3.8 3.3 1.1 4.9L8 11.8 3.6 14.3l1.1-4.9L.9 6.1l5-.5z" fill="#F7CA91"/></svg>
    </div>
    <div class="quote">&ldquo;</div>
    <p class="t-text">Lorem Ipsum is simply dummy text of the printing and typesetting industry. Lorem Ipsum has been the industry's standard dummy.</p>
  </article>
  <article class="testimonial" style="left:585px">
    <div class="avatar" style="background:linear-gradient(160deg,#d8c8b8,#8a7a6a)" role="img" aria-label="Guest portrait"></div>
    <div class="t-name">Owen T.</div>
    <div class="stars">
      <svg viewBox="0 0 16 16"><path d="M8 1l2.1 4.6 5 .5-3.8 3.3 1.1 4.9L8 11.8 3.6 14.3l1.1-4.9L.9 6.1l5-.5z" fill="#fff"/></svg>
      <svg viewBox="0 0 16 16"><path d="M8 1l2.1 4.6 5 .5-3.8 3.3 1.1 4.9L8 11.8 3.6 14.3l1.1-4.9L.9 6.1l5-.5z" fill="#fff"/></svg>
      <svg viewBox="0 0 16 16"><path d="M8 1l2.1 4.6 5 .5-3.8 3.3 1.1 4.9L8 11.8 3.6 14.3l1.1-4.9L.9 6.1l5-.5z" fill="#fff"/></svg>
      <svg viewBox="0 0 16 16"><path d="M8 1l2.1 4.6 5 .5-3.8 3.3 1.1 4.9L8 11.8 3.6 14.3l1.1-4.9L.9 6.1l5-.5z" fill="#fff"/></svg>
      <svg viewBox="0 0 16 16"><path d="M8 1l2.1 4.6 5 .5-3.8 3.3 1.1 4.9L8 11.8 3.6 14.3l1.1-4.9L.9 6.1l5-.5z" fill="#fff"/></svg>
    </div>
    <div class="quote">&ldquo;</div>
    <p class="t-text">Lorem Ipsum is simply dummy text of the printing and typesetting industry. Lorem Ipsum has been the industry's standard dummy.</p>
  </article>
  <article class="testimonial" style="left:986px">
    <div class="avatar" style="background:linear-gradient(160deg,#c8b8a8,#6a5a4a)" role="img" aria-label="Guest portrait"></div>
    <div class="t-name">Liam K.</div>
    <div class="stars">
      <svg viewBox="0 0 16 16"><path d="M8 1l2.1 4.6 5 .5-3.8 3.3 1.1 4.9L8 11.8 3.6 14.3l1.1-4.9L.9 6.1l5-.5z" fill="#fff"/></svg>
      <svg viewBox="0 0 16 16"><path d="M8 1l2.1 4.6 5 .5-3.8 3.3 1.1 4.9L8 11.8 3.6 14.3l1.1-4.9L.9 6.1l5-.5z" fill="#fff"/></svg>
      <svg viewBox="0 0 16 16"><path d="M8 1l2.1 4.6 5 .5-3.8 3.3 1.1 4.9L8 11.8 3.6 14.3l1.1-4.9L.9 6.1l5-.5z" fill="#fff"/></svg>
      <svg viewBox="0 0 16 16"><path d="M8 1l2.1 4.6 5 .5-3.8 3.3 1.1 4.9L8 11.8 3.6 14.3l1.1-4.9L.9 6.1l5-.5z" fill="#fff"/></svg>
      <svg viewBox="0 0 16 16"><path d="M8 1l2.1 4.6 5 .5-3.8 3.3 1.1 4.9L8 11.8 3.6 14.3l1.1-4.9L.9 6.1l5-.5z" fill="#fff"/></svg>
    </div>
    <div class="quote">&ldquo;</div>
    <p class="t-text">Lorem Ipsum is simply dummy text of the printing and typesetting industry. Lorem Ipsum has been the industry's standard dummy.</p>
  </article>

  <div class="btn btn-white" style="left:183px;top:432px;width:153px;height:31px">View more
    <svg viewBox="0 0 12 12" fill="none" stroke="currentColor" stroke-width="1.3"><path d="M1 6h10M7 2l4 4-4 4"/></svg></div>
</section>

<section class="section" style="top:3838px;height:270px;overflow:visible">
  <div class="photo" style="left:0;top:-32px;width:232px;height:166px;background:linear-gradient(180deg,#3a5a3e 0%,#2a4a34 45%,#2f8a8a 75%,#1e5a5e 100%)" role="img" aria-label="Boathouse pavilion on a turquoise forest lake"></div>
  <div class="photo" style="left:918px;top:43px;width:282px;height:187px;background:linear-gradient(160deg,#4a6a3a 0%,#8a8a6a 40%,#c8b89a 70%,#6a5a3a 100%)" role="img" aria-label="Aerial view of a lakeside hotel among autumn trees"></div>
  <h2 class="heading abs" style="left:0;width:1200px;text-align:center;top:56px;font-size:50px">Get in touch</h2>
  <div class="email">Enter your Email Address...</div>
  <div class="btn btn-orange" style="left:524px;top:188px;width:152px;height:31px">Submit
    <svg viewBox="0 0 12 12" fill="none" stroke="currentColor" stroke-width="1.3"><path d="M1 6h10M7 2l4 4-4 4"/></svg></div>
</section>

<footer class="section footer" style="top:4108px;height:380px">
  <div class="brand" style="top:76px;font-size:30px;color:var(--white)">Birch Hollow</div>
  <nav class="abs nav"><span>Home</span><span>About</span><span>Our vision</span><span>Explore</span><span>Live here</span><span>Locations</span></nav>
  <div class="social" style="left:488px" role="img" aria-label="Social profile link"></div>
  <div class="social" style="left:549px" role="img" aria-label="Social profile link"></div>
  <div class="social" style="left:610px" role="img" aria-label="Social profile link"></div>
  <div class="social" style="left:669px" role="img" aria-label="Social profile link"></div>
  <div class="abs" style="left:118px;top:292px;width:971px;height:1px;background:var(--orange)"></div>
  <p class="abs copyright">Copyright &copy; 2023 Northwind Studio LLC. All rights reserved.</p>
</footer>

</body>
</html>
```